House Cleaning Website - Maid Services

Logo, landing page design with contact form - coded MUST BE MOBILE FRIENDLY

Cleaning business - maid service - i've added a few example websites

Clean, Smart Website Design that is built for getting leads

CONTENT FOR HOME PAGE -

Cleaning Seminole County Homes For Over 12 Years

Rosetta Cleans

* Trusted by your neighbors for more than a decade
* Affordable and flexible to accommodate your needs
* 200% Money Back Guarantee
* Up to 20% Discount on Continued Cleanings
* Same Day Cleanings

My Clients Are Happy
"Rosetta has been cleaning my home for the past 3 1/2 years and I couldn't be happier with her. I trust her with cleaning my home while I'm out of town and recommend her to my friends."

Target Market(s)

people looking for house cleaning

Industry/Entity Type

Cleaning Service

Contact Information for Business Card

Rosetta Cleans -
#321-555-0187
200% Guarantee
on back of card - $25 Referral Fee

Logo Text

Rosetta Cleans

Coding

Coded - Design and coding required

Number of Pages Required

3 page

Requirements
Must have
• 4 links in top toolbar - services, contact, free estimate and about
• *contact will be a popup form to contact
• *services will be a graphic similar to the one on this page ... https://www.brightbroomcrew.com/maid-services/
• *free estimate link will be a page with same questions as
• Must have landing page concept - I will be advertising to get people to submit their information...
• 1. Must have a "Request FREE Estimate" button that pops up a box for them to submit their information - name, number, email. Once they submit this information, they will be taken to a 2nd form to complete their details - If they dont complete the 2nd part I still receive the 1st part to call. The 2nd part will have same questions ashttps://www.tidyhenwick.com/local-house-cleaning/fl/west-miami/request-a-cleaning.aspx?cpgnId=FE0CA3B4-3A4C-4D9C-9B11-E69492B42092&scid=3554195&cid=2303288&tc=17072613580054989&rl_key=a0563857ec931d2a952e39d66a08939d&kw=77903:7716&pub_cr_id=200261568213&dynamic_proxy=1&primary_serv=www.tidyhenwick.com&rl_track_landing_pages=1
• 2. Must have pricing like https://www.brightbroomcrew.com/ 1 bedroom through 6 bedroom pricing base pricing graphic.
• 2.Must have a 200% satisfaction guarantee graphic
• 3.Must have phone number visible
• 4. graphics offering - 1st deep clean $25 Off - 10% Off Bi Weekly Cleanings - 20% Off Weekly Cleanings
• I like the clean look of this website https://www.pearlofsuds.com/ BUT want a more compact website like https://www.brightbroomcrew.com/
• Popup for when the try and x out saying Book Now And Receive $20 Off 1st Cleaning

```html
<!DOCTYPE html>
<html lang="en">
<head>
<meta charset="utf-8">
<title>Rosetta Cleans</title>
<link rel="stylesheet" href="https://fonts.googleapis.com/css2?family=Montserrat:wght@500;600;700&family=Poppins:wght@400;500&family=Roboto+Slab:wght@400;500;700&display=swap">
<style>
:root{
  --teal:#1795b3;
  --teal-bar:#0aa0bd;
  --teal-btn:#2fc4dc;
  --coupon:#7fd0d6;
  --coupon-ink:#0f4d5b;
  --ink:#333;
  --muted:#555;
  --panel:#f6f6f6;
  --footer:#232323;
  --footer-ink:#bbb;
  --badge:#1a74c0;
}
*{margin:0;padding:0;box-sizing:border-box}
html,body{width:973px;height:1200px;overflow:hidden;background:#fff}
body{position:relative;font-family:'Poppins',sans-serif;color:var(--ink)}
.abs{position:absolute}
.site-header{position:absolute;left:0;top:0;width:973px;height:67px;background:#fff}
.brand{left:79px;top:22px;display:flex;align-items:center;gap:7px;font-family:'Roboto Slab',serif;font-weight:700;font-size:14px;color:var(--teal)}
.brand-dot{width:22px;height:22px;border-radius:50%;background:#f5c542}
.phone{left:736px;top:9px;display:flex;align-items:center;gap:8px;font-family:'Montserrat',sans-serif;font-weight:500;font-size:19px;color:#333}
.nav a{position:absolute;top:47px;font-family:'Montserrat',sans-serif;font-weight:500;font-size:11.5px;color:#333;text-decoration:none;transform:translateX(-50%)}
.hero{left:0;top:67px;width:973px;height:385px;background:linear-gradient(90deg,#cfc9c1 0%,#bdb6ad 40%,#9b9288 55%,#c9c2b8 75%,#b5aca1 100%)}
.hero-shade{position:absolute;inset:0;background:rgba(60,55,50,.28)}
.hero h1{position:absolute;left:0;width:973px;top:117px;text-align:center;font-family:'Montserrat',sans-serif;font-weight:700;font-size:32px;line-height:55px;color:#fff;letter-spacing:.5px}
.hero-btn{position:absolute;left:296px;top:238px;width:368px;height:49px;border:1px solid #fff;color:#fff;font-family:'Montserrat',sans-serif;font-weight:500;font-size:19px;display:flex;align-items:center;justify-content:center}
.intro h2{position:absolute;left:91px;top:508px;font-family:'Montserrat',sans-serif;font-weight:600;font-size:21px;color:var(--teal)}
.perks{position:absolute;left:91px;top:551px;list-style:none}
.perks li{height:28px;font-size:10.5px;color:var(--muted);display:flex;align-items:center;gap:10px}
.perks li::before{content:"";border-left:4px solid #666;border-top:3.5px solid transparent;border-bottom:3.5px solid transparent}
.prices{left:432px;top:494px;width:446px;height:200px;background:var(--panel)}
.prices-head{height:41px;background:var(--teal-bar);color:#fff;font-family:'Roboto Slab',serif;font-size:14px;display:flex;align-items:center;justify-content:center}
.price-cols{display:flex;justify-content:space-between;padding:20px 16px 0 20px;font-family:'Roboto Slab',serif;text-align:center}
.price-col{width:62px;color:#333}
.price-col .n{font-size:13px;height:24px}
.price-col .b{font-size:10.5px;height:31px}
.price-col .p{font-family:'Poppins',sans-serif;font-size:11px}
.book-btn{position:absolute;left:141px;top:155px;width:166px;height:28px;background:var(--teal-btn);color:#fff;font-family:'Roboto Slab',serif;font-weight:700;font-size:11px;display:flex;align-items:center;justify-content:center}
.coupon{top:739px;width:261px;height:169px;background:linear-gradient(135deg,#8ed7dc,#6cc6cf 60%,#5ab8c2);color:var(--coupon-ink);font-family:'Roboto Slab',serif;text-align:center}
.coupon::after{content:"";position:absolute;inset:14px;border:2px dashed #1a7f93}
.coupon .big{position:absolute;left:0;right:0;top:54px;font-size:31px;font-weight:500}
.coupon .sub{position:absolute;left:0;right:0;top:98px;font-size:15.5px;font-weight:500;letter-spacing:.5px}
.testimonials h3{position:absolute;left:0;width:973px;top:940px;text-align:center;font-family:'Montserrat',sans-serif;font-weight:500;font-size:21px;color:var(--teal)}
.quote{position:absolute;left:170px;width:633px;top:981px;text-align:center;font-size:10.5px;line-height:26px;color:#333}
.site-footer{left:0;top:1073px;width:973px;height:127px;background:var(--footer)}
.social{position:absolute;top:26px;width:24px;height:24px;border:1.5px solid #ddd;border-radius:50%}
.foot-links a{position:absolute;top:70px;transform:translateX(-50%);font-family:'Montserrat',sans-serif;font-size:10px;color:var(--footer-ink);text-decoration:none}
.copyright{position:absolute;left:0;width:973px;top:101px;text-align:center;font-family:'Montserrat',sans-serif;font-size:10px;color:var(--footer-ink)}
.badge{left:791px;top:980px}
</style>
</head>
<body>
<header class="site-header">
  <div class="abs brand"><span class="brand-dot"></span>Rosetta Cleans</div>
  <div class="abs phone">
    <svg width="22" height="22" viewBox="0 0 22 22"><circle cx="11" cy="11" r="10" fill="none" stroke="#1795b3" stroke-width="1.6"/><path d="M7.5 6.5c.6-.6 1.3-.5 1.7.1l.9 1.5c.3.5.2 1-.2 1.4l-.6.5c.5 1.2 1.5 2.2 2.7 2.7l.5-.6c.4-.4.9-.5 1.4-.2l1.5.9c.6.4.7 1.1.1 1.7-1 1-2.3 1.2-3.6.5-2-1.1-3.6-2.7-4.7-4.7-.7-1.3-.5-2.6.3-3.8z" fill="#1795b3"/></svg>
    1800 555 019
  </div>
  <nav class="nav">
    <a href="#" style="left:560px">Services</a>
    <a href="#" style="left:657px">Contact</a>
    <a href="#" style="left:770px">Free Estimate</a>
    <a href="#" style="left:877px">About</a>
  </nav>
</header>

<section class="abs hero" role="img" aria-label="Photo of a person holding a mop and cleaning bucket in a bright room">
  <div class="hero-shade"></div>
  <h1>Cleaning Seminole County Homes For<br>Over 12 Years</h1>
  <div class="hero-btn">Request Free Estimate</div>
</section>

<section class="intro">
  <h2>Rosetta Cleans</h2>
  <ul class="perks">
    <li>Trusted by your neighbors for more than a decade</li>
    <li>Affordable and flexible to accommodate your needs</li>
    <li>200% Money Back Guarantee</li>
    <li>Up to 20% Discount on Continued Cleanings</li>
    <li>Same Day Cleanings</li>
  </ul>
</section>

<section class="abs prices">
  <div class="prices-head">Check Our Prices</div>
  <div class="price-cols">
    <div class="price-col"><div class="n">1</div><div class="b">Bedroom</div><div class="p">$85</div></div>
    <div class="price-col"><div class="n">2</div><div class="b">Bedroom</div><div class="p">$90</div></div>
    <div class="price-col"><div class="n">3</div><div class="b">Bedroom</div><div class="p">$105</div></div>
    <div class="price-col"><div class="n">4</div><div class="b">Bedroom</div><div class="p">$120</div></div>
    <div class="price-col"><div class="n">5</div><div class="b">Bedroom</div><div class="p">$150</div></div>
    <div class="price-col"><div class="n">6</div><div class="b">Bedroom</div><div class="p">$200</div></div>
  </div>
  <div class="book-btn">BOOK IN 60 SEC</div>
</section>

<section class="offers">
  <div class="abs coupon" style="left:80px"><div class="big">$25 Off</div><div class="sub">1st Deep Clean</div></div>
  <div class="abs coupon" style="left:354px"><div class="big">10% Off</div><div class="sub">Bi Weekly Cleanings</div></div>
  <div class="abs coupon" style="left:633px"><div class="big">20% Off</div><div class="sub">Weekly Cleanings</div></div>
</section>

<section class="testimonials">
  <h3>Our Testimonials</h3>
  <p class="quote">Rosetta has been cleaning my home for the past 3 1/2 years and I couldn't be happier with her. I trust her with cleaning my home while I'm out of town and recommend her to my friends."<br>- My Clients Are Happy</p>
</section>

<footer class="abs site-footer">
  <span class="social" style="left:424px"></span>
  <span class="social" style="left:458px"></span>
  <span class="social" style="left:491px"></span>
  <span class="social" style="left:525px"></span>
  <nav class="foot-links">
    <a href="#" style="left:236px">FAQ</a>
    <a href="#" style="left:297px">Blog</a>
    <a href="#" style="left:389px">Terms of Service</a>
    <a href="#" style="left:504px">Privacy Policy</a>
    <a href="#" style="left:586px">Jobs</a>
    <a href="#" style="left:653px">Log In</a>
    <a href="#" style="left:726px">Sitemap</a>
  </nav>
  <div class="copyright">© 2017 Rosetta Cleans. All Rights Reserved</div>
</footer>

<svg class="abs badge" width="132" height="132" viewBox="0 0 132 132" role="img" aria-label="Satisfaction guarantee seal">
  <circle cx="66" cy="66" r="64" fill="#fff"/>
  <circle cx="66" cy="66" r="60" fill="var(--badge)"/>
  <circle cx="66" cy="66" r="50" fill="none" stroke="#fff" stroke-width="1.5" stroke-dasharray="2 3"/>
</svg>
</body>
</html>
```